Professional Consulting Firm Business Card Design

We need a business card design for a new professional consulting firm that specializes in petroleum, health, and financial consulting. We need a design that is trendy but elegant, and one that would make a summit 300 executive feel comfortable using our services. I have attached a logo that needs to be used in the design. I have also attached a photo of a card design that I like.

On the card we need a place for employee name, title, email address, fax number, phone number, mailing address, and website address.

Industry/Entity Type

Financial

Contact Information for Business Card

see attached

Other font styles liked:
• Calibri or your choice

Requirements
Must have
• style
Nice to have
• texture, rounded edges
Should not have
• no solid black cards but black may be used

```html
<!DOCTYPE html>
<html lang="en">
<head>
<meta charset="UTF-8">
<title>Ridgeway Consulting LLC – Business Card</title>
<link rel="stylesheet" href="https://fonts.googleapis.com/css2?family=Urbanist:wght@400;500;700&display=swap">
<style>
  :root {
    --backdrop: #e6e7e9;
    --card: #f8f9fa;
    --card-edge: #d9dce0;
    --navy: #122c55;
    --ink: #3a3d42;
    --band: #0f2a52;
  }
  * { margin: 0; padding: 0; box-sizing: border-box; }
  html, body {
    width: 1200px;
    height: 970px;
    overflow: hidden;
    background: var(--backdrop);
    font-family: "Urbanist", "Century Gothic", sans-serif;
  }
  .card {
    position: absolute;
    left: 120px;
    top: 218px;
    width: 960px;
    height: 534px;
    background: var(--card);
    border: 1px solid var(--card-edge);
    border-radius: 6px;
    overflow: hidden;
    box-shadow: 0 18px 40px rgba(20, 30, 50, 0.12);
  }
  .brand {
    position: absolute;
    left: 144px;
    top: 78px;
    color: var(--navy);
  }
  .brand-name {
    font-size: 50px;
    font-weight: 500;
    letter-spacing: 1px;
    line-height: 1;
  }
  .brand-tagline {
    margin-top: 10px;
    font-size: 13.5px;
    font-weight: 500;
    letter-spacing: 0.3px;
    text-transform: uppercase;
  }
  .person {
    position: absolute;
    left: 46px;
    top: 308px;
    color: var(--ink);
  }
  .person-name {
    font-size: 25px;
    font-weight: 700;
    color: var(--navy);
    line-height: 1.1;
  }
  .person-title {
    font-size: 21px;
    font-weight: 400;
    margin-top: 2px;
  }
  .contact-list {
    list-style: none;
    margin-top: 28px;
    font-size: 21px;
    line-height: 28px;
  }
  .contact-list li {
    display: flex;
    align-items: center;
    gap: 8px;
  }
  .contact-list svg {
    width: 16px;
    height: 16px;
    fill: var(--navy);
    flex: none;
  }
  .office {
    position: absolute;
    left: 594px;
    top: 340px;
    font-size: 21px;
    line-height: 28px;
    color: var(--ink);
  }
  .office-web {
    margin-top: 16px;
    letter-spacing: 1.6px;
  }
  .card-band {
    position: absolute;
    left: 0;
    bottom: 0;
    width: 100%;
    height: 34px;
    background: var(--band);
  }
</style>
</head>
<body>
  <section class="card">
    <header class="brand">
      <div class="brand-name">RIDGEWAY CONSULTING LLC</div>
      <div class="brand-tagline">Health, Safety, and Financial Consulting Services</div>
    </header>

    <div class="person">
      <div class="person-name">Daniel R. Whitford</div>
      <div class="person-title">Managing Director</div>
      <ul class="contact-list">
        <li>
          <svg viewBox="0 0 16 16" aria-hidden="true"><path d="M3.6 1.5l2.2 2.6c.3.4.3.9 0 1.3L4.7 6.6c.9 2 2.6 3.8 4.7 4.7l1.2-1.1c.4-.3.9-.3 1.3 0l2.6 2.2c.4.4.4 1 0 1.4l-1.2 1.2C10.5 16 0 5.5 1 2.7L2.2 1.5c.4-.4 1-.4 1.4 0z"/></svg>
          + 999 999 9999
        </li>
        <li>
          <svg viewBox="0 0 16 16" aria-hidden="true"><path d="M4 1h8v4H4zM1 6h14v6h-3v3H4v-3H1zM5 10v4h6v-4z"/></svg>
          + 999 999 9999
        </li>
        <li>
          <svg viewBox="0 0 16 16" aria-hidden="true"><path d="M1 3h14v10H1zM2.5 4.5v.3L8 9l5.5-4.2v-.3zM2.5 6.7v4.8h11V6.7L8 10.9z"/></svg>
          info@ridgewayconsulting.com
        </li>
      </ul>
    </div>

    <address class="office" style="font-style: normal;">
      <div>415 Larkspur Ave., Ste. 1200 North</div>
      <div>Denver Colorado 80215</div>
      <div class="office-web">www.ridgewayconsulting.com</div>
    </address>

    <div class="card-band"></div>
  </section>
</body>
</html>
```